Luxury Brand Real Estate For Sale sign

**Update** I've added some examples from the internet of other signs that have a look similar to what I would like to see. I do not want my personal name in the sign. And the word FOR SALE Does not need to be so large - it can be more subtle.
I want to create a Real Estate for sale sign for my company that will be used for luxury/higher end real estate listings. I’m sharing my business card as well as a logo with new teal color to show what we're moving towards: we’re using Teal, white, black and gold.
Hoping the sign is simple, sophisticated and eye catching.
The sign should be 24" wide by 30" tall including the company name: Harbor Crest Realty Group and our logo, office phone number 727-555-0148 and website www.hcrgexample.com the words "For Sale"
Optional to add this e-mail address info@hcrgexample.com to the sign
Target Market(s)
Luxury home buyers
Industry/Entity Type
Real Estate
Look and feel

```html
<!DOCTYPE html>
<html lang="en">
<head>
<meta charset="utf-8">
<title>Harbor Crest Realty Group – For Sale Sign</title>
<link rel="stylesheet" href="https://fonts.googleapis.com/css2?family=Montserrat:wght@300;400;600;800&family=Raleway:wght@300;400&display=swap">
<style>
  :root {
    --page-bg: #eef1f2;
    --sign-border: #f4f9fc;
    --sign-border-tint: #dcedf7;
    --teal: #0b8582;
    --teal-shadow: #08706d;
    --ink-light: #f3f8fa;
    --bar-grey: #4a4a4c;
  }
  * { box-sizing: border-box; margin: 0; padding: 0; }
  html, body {
    width: 1200px; height: 1200px; overflow: hidden;
    background: var(--page-bg);
  }
  .sign {
    position: absolute; left: 220px; top: 125px;
    width: 760px; height: 950px;
    background: linear-gradient(160deg, var(--sign-border-tint), var(--sign-border) 40%, var(--sign-border) 70%, var(--sign-border-tint));
    box-shadow: 0 10px 30px rgba(0,0,0,0.12);
  }
  .panel {
    position: absolute; left: 40px; top: 40px;
    width: 680px; height: 870px;
    background: var(--teal);
    color: var(--ink-light);
  }
  .brand {
    position: absolute; left: 72px; top: 82px;
    display: flex; align-items: center; height: 116px;
  }
  .brand-mark {
    display: flex; align-items: center; gap: 10px;
    font-family: "Raleway", sans-serif; font-weight: 300;
    font-size: 38px; letter-spacing: 1px;
  }
  .brand-square {
    width: 16px; height: 16px; border: 2px solid var(--ink-light);
  }
  .brand-divider {
    width: 2px; height: 116px; background: var(--ink-light);
    margin: 0 26px 0 26px;
  }
  .brand-name {
    font-family: "Raleway", sans-serif; font-weight: 300;
    line-height: 1;
  }
  .brand-name .line-main { font-size: 27px; letter-spacing: 0.5px; }
  .brand-name .line-sub { font-size: 16px; letter-spacing: 8px; margin-top: 12px; }
  .headline {
    position: absolute; left: 72px; top: 248px;
    font-family: "Montserrat", sans-serif; font-weight: 800;
    font-size: 150px; line-height: 160px; letter-spacing: -2px;
    text-shadow: 6px 6px 0 var(--teal-shadow);
  }
  .phone {
    position: absolute; left: 78px; top: 618px;
    font-family: "Montserrat", sans-serif; font-weight: 800;
    font-size: 70px; letter-spacing: -2px;
  }
  .web-bar {
    position: absolute; left: 80px; top: 724px;
    width: 494px; height: 92px;
    background: var(--bar-grey);
    display: flex; align-items: center; justify-content: center;
    font-family: "Montserrat", sans-serif; font-weight: 300;
    font-size: 31px; letter-spacing: 1px;
  }
  .web-bar strong { font-weight: 600; }
</style>
</head>
<body>
  <div class="sign">
    <div class="panel">
      <div class="brand">
        <div class="brand-mark"><span class="brand-square"></span>HCRG</div>
        <div class="brand-divider"></div>
        <div class="brand-name">
          <div class="line-main">HARBOR CREST</div>
          <div class="line-sub">REALTY GROUP</div>
        </div>
      </div>
      <h1 class="headline">FOR<br>SALE</h1>
      <div class="phone">727-555-0148</div>
      <div class="web-bar">www.<strong>hcrgexample</strong>.com</div>
    </div>
  </div>
</body>
</html>
```